Financial Advisor needs waiting room sign

I am a financial advisor that works with a number of accountants to develop prospects. I am looking for a 18"x24" sign to hang in their office waiting rooms to help develop prospect interest in my services. My original idea was to list all of our services in a jumbled way on the sign and on the bottom have something like "Confused? We have the answers?" "Questions - We have answers" Our logo on the bottom. While I think this is still a good idea when I try to design it - it does not work. I am open to other ideas. Here is a list of our services (list in no particular order) and I will attach our logo. List: Vellorin, Vellorin Supplement, Vellorin Advantage, Tolquist, Part A, Part B, Part D, Social Security, Turning 65, Annuities, Fixed Index Annuities, Rollovers, 401k, 403b, Investments, Stock Market, Mutual Funds, Term Insurance, Life Insurance, Final Expense, Long Term Care, Mortgage Protection, 403B / 457 Not for Profit Set Up, 403B / TSA Plans, Annuities, Asset Protection, Charitable Giving, College Funding, Estate Planning, Fixed Indexed Annuities, Guaranteed Income, IRA & 401(K) Assets and Planning, IRA, 401(K), 403(B) Rollovers, Lifetime Income Planning, Retirement Income Planning, Safe Money Options, Social Security, Tactical Asset Allocation

```html
<!DOCTYPE html>
<html lang="en">
<head>
<meta charset="utf-8">
<title>Hollowbrook Capital – Waiting Room Sign</title>
<link href="https://fonts.googleapis.com/css2?family=Montserrat:wght@800&family=Roboto+Condensed:wght@400;700&display=swap" rel="stylesheet">
<style>
  :root {
    --green: #6cb13f;
    --green-dark: #4f8a2b;
    --gray: #58595b;
    --white: #ffffff;
    --paper-top: #e3e4e6;
    --paper: #ffffff;
  }
  html, body { margin: 0; padding: 0; overflow: hidden; background: var(--paper); }
  .sign { display: block; width: 1200px; height: 955px; }
  .headline { font-family: "Montserrat", sans-serif; font-weight: 800; fill: var(--gray); }
  .tagline-band { fill: var(--green); }
  .tagline { font-family: "Montserrat", sans-serif; font-weight: 800; fill: var(--white); }
  .term { font-family: "Roboto Condensed", sans-serif; }
  .bold { font-weight: 700; }
  .regular { font-weight: 400; }
  .green { fill: var(--green); }
  .green-dark { fill: var(--green-dark); }
  .gray { fill: var(--gray); }
  .brand-mark { fill: var(--green); }
  .brand-rule { stroke: var(--gray); stroke-width: 1.5; }
  .brand-name { font-family: "Roboto Condensed", sans-serif; font-weight: 700; fill: var(--green-dark); }
  .brand-sub { font-family: "Roboto Condensed", sans-serif; font-weight: 700; fill: var(--gray); }
</style>
</head>
<body>
<svg class="sign" viewBox="0 0 1200 955" xmlns="http://www.w3.org/2000/svg" role="img" aria-label="Confused? We have the answers? — a word cloud of insurance and financial services by Hollowbrook Capital">
  <defs>
    <linearGradient id="paper-fade" x1="0" y1="0" x2="0" y2="1">
      <stop offset="0" stop-color="var(--paper-top)"/>
      <stop offset="0.35" stop-color="#f4f4f5"/>
      <stop offset="1" stop-color="var(--paper)"/>
    </linearGradient>
  </defs>

  <!-- background -->
  <rect width="1200" height="955" fill="url(#paper-fade)"/>

  <!-- headline -->
  <text class="headline" x="128" y="146" font-size="134" textLength="943" lengthAdjust="spacingAndGlyphs">CONFUSED?</text>

  <!-- tagline band -->
  <rect class="tagline-band" x="0" y="172" width="1200" height="65"/>
  <text class="tagline" x="282" y="219" font-size="44" textLength="635" lengthAdjust="spacingAndGlyphs">WE HAVE THE ANSWERS?</text>

  <!-- service word cloud -->
  <g class="services">
    <text class="term bold green" x="182" y="309" font-size="48" textLength="196" lengthAdjust="spacingAndGlyphs">MORTGAGE</text>
    <text class="term bold gray" x="388" y="306" font-size="44" textLength="178" lengthAdjust="spacingAndGlyphs">Annuities</text>
    <text class="term bold green" x="574" y="309" font-size="52" textLength="361" lengthAdjust="spacingAndGlyphs">SOCIAL SECURITY</text>
    <text class="term bold green" x="159" y="358" font-size="54" textLength="221" lengthAdjust="spacingAndGlyphs">PROTECTION</text>
    <text class="term regular gray" x="156" y="394" font-size="42" textLength="224" lengthAdjust="spacingAndGlyphs">Charitable Giving</text>
    <text class="term bold green" x="260" y="444" font-size="53" textLength="120" lengthAdjust="spacingAndGlyphs">403B /</text>
    <text class="term bold green" x="182" y="489" font-size="53" textLength="198" lengthAdjust="spacingAndGlyphs">TSA PLANS</text>
    <text class="term bold green" transform="translate(118 397) rotate(90)" font-size="33" textLength="227" lengthAdjust="spacingAndGlyphs">LIFETIME INCOME</text>
    <text class="term bold green" transform="translate(81 493) rotate(90)" font-size="32" textLength="129" lengthAdjust="spacingAndGlyphs">PLANNING</text>
    <text class="term bold gray" x="156" y="530" font-size="40" textLength="224" lengthAdjust="spacingAndGlyphs">403(B) Rollovers</text>
    <text class="term bold green" x="151" y="585" font-size="54" textLength="126" lengthAdjust="spacingAndGlyphs">ESTATE</text>
    <text class="term bold green" x="151" y="617" font-size="35" textLength="126" lengthAdjust="spacingAndGlyphs">PLANNING</text>
    <text class="term bold green" x="122" y="677" font-size="62" textLength="155" lengthAdjust="spacingAndGlyphs">SOCIAL</text>
    <text class="term bold green" x="66" y="729" font-size="62" textLength="211" lengthAdjust="spacingAndGlyphs">SECURITY</text>
    <text class="term bold green" transform="translate(287 543) rotate(90)" font-size="55" textLength="196" lengthAdjust="spacingAndGlyphs">FUNDING</text>
    <text class="term bold green" transform="translate(336 543) rotate(90)" font-size="52" textLength="196" lengthAdjust="spacingAndGlyphs">COLLEGE</text>
    <text class="term bold green" transform="translate(388 320) rotate(90)" font-size="55" textLength="342" lengthAdjust="spacingAndGlyphs">FINAL EXPENSE</text>

    <text class="term bold green" x="439" y="379" font-size="88" textLength="350" lengthAdjust="spacingAndGlyphs">VELLORIN</text>
    <text class="term" x="437" y="418" font-size="29" textLength="355" lengthAdjust="spacingAndGlyphs"><tspan class="regular gray">IRA, 401(K), </tspan><tspan class="bold green">Vellorin Supplement</tspan></text>
    <text class="term bold green" x="439" y="463" font-size="48" textLength="350" lengthAdjust="spacingAndGlyphs">Vellorin Advantage</text>
    <text class="term bold green" transform="translate(837 470) rotate(-90)" font-size="50" textLength="152" lengthAdjust="spacingAndGlyphs">Tolquist</text>

    <text class="term bold gray" x="851" y="355" font-size="48" textLength="90" lengthAdjust="spacingAndGlyphs">401k</text>
    <text class="term bold gray" x="851" y="379" font-size="25" textLength="56" lengthAdjust="spacingAndGlyphs">403b</text>
    <text class="term bold green" x="952" y="383" font-size="44" textLength="180" lengthAdjust="spacingAndGlyphs">Guaranteed</text>
    <text class="term regular gray" x="849" y="426" font-size="48" textLength="161" lengthAdjust="spacingAndGlyphs">ANNUITIES</text>
    <text class="term bold green" x="1018" y="423" font-size="44" textLength="113" lengthAdjust="spacingAndGlyphs">Income</text>
    <text class="term bold green" x="849" y="480" font-size="68" textLength="287" lengthAdjust="spacingAndGlyphs">ROLLOVERS</text>

    <text class="term regular gray" x="437" y="506" font-size="35" textLength="176" lengthAdjust="spacingAndGlyphs">STOCK MARKET</text>
    <text class="term bold green" x="437" y="541" font-size="37" textLength="176" lengthAdjust="spacingAndGlyphs">Mutual Funds</text>
    <text class="term bold gray" x="437" y="574" font-size="35" textLength="174" lengthAdjust="spacingAndGlyphs">Life Insurance</text>
    <text class="term bold green" x="437" y="632" font-size="56" textLength="177" lengthAdjust="spacingAndGlyphs">FIXED INDEXED</text>
    <text class="term bold green" x="437" y="684" font-size="56" textLength="125" lengthAdjust="spacingAndGlyphs">ANNUITIES</text>
    <text class="term bold green" transform="translate(652 694) rotate(-90)" font-size="50" textLength="214" lengthAdjust="spacingAndGlyphs">Turning 65</text>

    <text class="term bold green" x="670" y="517" font-size="50" textLength="174" lengthAdjust="spacingAndGlyphs">Part A,B,D</text>
    <text class="term bold green-dark" x="845" y="515" font-size="35" textLength="170" lengthAdjust="spacingAndGlyphs">INVESTMENTS</text>
    <text class="term regular gray" x="670" y="566" font-size="48" textLength="344" lengthAdjust="spacingAndGlyphs">Fixed Index Annuities</text>
    <text class="term bold green-dark" x="670" y="601" font-size="32" textLength="344" lengthAdjust="spacingAndGlyphs">TERM INSURANCE, IRA, 401(K)</text>
    <text class="term regular green" x="670" y="637" font-size="32" textLength="341" lengthAdjust="spacingAndGlyphs">IRA &amp; 401(K) Assets and Planning</text>
    <text class="term bold green" x="670" y="686" font-size="52" textLength="337" lengthAdjust="spacingAndGlyphs">ASSET PROTECTION</text>

    <text class="term bold green" transform="translate(1023 493) rotate(90)" font-size="35" textLength="246" lengthAdjust="spacingAndGlyphs">LONG TERM CARE</text>
    <text class="term regular gray" transform="translate(1060 493) rotate(90)" font-size="36" textLength="243" lengthAdjust="spacingAndGlyphs">Income Planning</text>
    <text class="term regular gray" transform="translate(1099 493) rotate(90)" font-size="36" textLength="163" lengthAdjust="spacingAndGlyphs">Retirement</text>

    <text class="term regular gray" x="390" y="736" font-size="56" textLength="617" lengthAdjust="spacingAndGlyphs">403B / 457 Not for Profit Set Up</text>
    <text class="term regular gray" x="184" y="791" font-size="48" textLength="398" lengthAdjust="spacingAndGlyphs">Tactical Asset Allocation</text>
    <text class="term bold green" x="591" y="794" font-size="62" textLength="541" lengthAdjust="spacingAndGlyphs">SAFE MONEY OPTIONS</text>
  </g>

  <!-- brand -->
  <g class="brand">
    <circle class="brand-mark" cx="352" cy="871" r="38"/>
    <line class="brand-rule" x1="405" y1="846" x2="405" y2="903"/>
    <text class="brand-name" x="418" y="875" font-size="31" textLength="468" lengthAdjust="spacingAndGlyphs">HOLLOWBROOK CAPITAL</text>
    <text class="brand-sub" x="418" y="898" font-size="13" textLength="468" lengthAdjust="spacing">INSURANCE AND FINANCIAL SERVICES</text>
  </g>
</svg>
</body>
</html>
```